label update for bottle change

The goal is to adapt the label's design and shape to the new bottle, maintaining its defining elements such as the font, vertical name, company logo, background pattern, and color. The new design should not be identical to the old one, but rather an evolution of it. The gold stripe on the bottom is not mandatory, but the writing "CASTELVENTO DEL MONTE / EST. 1886" must be retained, slightly enlarged.

The font name is: Brandon Text

```html
<!DOCTYPE html>
<html lang="it">
<head>
<meta charset="utf-8">
<title>Amaro di Carattere – Carciofo label</title>
<link rel="stylesheet" href="https://fonts.googleapis.com/css2?family=Josefin+Sans:wght@300;700&family=Lilita+One&display=swap">
<style>
  :root {
    --page-bg: #e4e4e4;
    --label-purple: #4a1466;
    --label-purple-deep: #3a0d52;
    --pattern-tone: #5e2a7c;
    --ink-white: #ffffff;
    --gold-light: #f3e2a0;
    --gold-mid: #d9b65c;
    --gold-dark: #b88a2e;
    --band-ink: #3b2a0e;
  }
  * { margin: 0; padding: 0; box-sizing: border-box; }
  html, body {
    width: 1200px; height: 1200px; overflow: hidden;
    background: var(--page-bg);
  }
  .label {
    position: absolute;
    left: 215px; top: 72px;
    width: 770px; height: 1053px;
    overflow: hidden;
    color: var(--ink-white);
    text-align: center;
  }
  .label__pattern {
    position: absolute; inset: 0;
    background:
      radial-gradient(circle at 50% 45%, var(--pattern-tone) 0%, var(--label-purple) 55%, var(--label-purple-deep) 100%);
  }
  .maker {
    position: absolute; left: 0; right: 0; top: 150px;
  }
  .maker__trade {
    font-family: "Josefin Sans", sans-serif;
    font-weight: 700;
    font-size: 15px;
    letter-spacing: 5px;
    line-height: 1;
  }
  .maker__name {
    margin-top: 6px;
    font-family: "Josefin Sans", sans-serif;
    font-weight: 700;
    font-size: 34px;
    letter-spacing: 1px;
    line-height: 1;
  }
  .tagline {
    position: absolute; left: 0; right: 0; top: 208px;
    font-family: "Josefin Sans", sans-serif;
    font-weight: 300;
    font-size: 36px;
    letter-spacing: 1px;
    line-height: 1;
  }
  .product-name {
    position: absolute; left: 0; right: 0; top: 268px;
    font-family: "Lilita One", sans-serif;
    font-size: 150px;
    line-height: 138px;
    letter-spacing: 4px;
  }
  .illustration {
    position: absolute;
    left: 150px; top: 595px;
    width: 420px; height: 440px;
  }
  .origin-band {
    position: absolute; left: 0; right: 0; top: 960px;
    height: 44px;
    background: linear-gradient(90deg, var(--gold-dark), var(--gold-light) 45%, var(--gold-mid) 75%, var(--gold-dark));
    display: flex; align-items: center; justify-content: center;
    font-family: "Josefin Sans", sans-serif;
    font-weight: 300;
    font-size: 25px;
    letter-spacing: 0.5px;
    color: var(--band-ink);
  }
</style>
</head>
<body>
  <section class="label">
    <div class="label__pattern" role="img" aria-label="Purple background with a repeating floral star pattern"></div>

    <header class="maker">
      <p class="maker__trade">FABBRICA LIQUORI</p>
      <p class="maker__name">F.LLI VALDORO</p>
    </header>

    <p class="tagline">AMARO DI CARATTERE</p>

    <h1 class="product-name">CAR<br>CIOFO</h1>

    <svg class="illustration" viewBox="0 0 420 440" role="img" aria-label="Gold line illustration of a lotus flower on a long stem">
      <defs>
        <radialGradient id="gold-glow" cx="50%" cy="40%" r="55%">
          <stop offset="0%" stop-color="#e8c874" stop-opacity="0.55"/>
          <stop offset="100%" stop-color="#e8c874" stop-opacity="0"/>
        </radialGradient>
      </defs>
      <rect width="420" height="440" fill="url(#gold-glow)"/>
    </svg>

    <div class="origin-band">CASTELVENTO DEL MONTE / EST. 1886</div>
  </section>
</body>
</html>
```